French for French

Cover for the book "The Plume Vagabonde" ("How to write in French"). The book seeks to teach English to English: words, grammar, syntax. The lessons are pleasant, the style is very classical.

Target Market(s)

Middle class interested in improving her language.

Industry/Entity Type

Publishing Company

Colors

Designer to choose colors to be used in the design.

Requirements
Must have
• Author: "Bernard Morlaix" Title: "The Lively Pen" Publisher: "Quillon Editions" Size: 14 x 20,5 cm

```html
<!DOCTYPE html>
<html lang="fr">
<head>
<meta charset="utf-8">
<title>Plume Vagabonde — Bernard Morlaix</title>
<link rel="stylesheet" href="https://fonts.googleapis.com/css2?family=Cormorant+Garamond:wght@500;600&family=Marcellus&display=swap">
<style>
  :root {
    --paper: #efeeec;
    --title-blue: #344e64;
    --author-brown: #3b2c1c;
    --flag-blue: #1f4f9c;
    --flag-white: #e9e8e6;
    --flag-red: #c9311c;
    --wreath-green: #b9c7a6;
    --wreath-pale: #e4e8dc;
    --ink: #2a2520;
  }
  * { margin: 0; padding: 0; box-sizing: border-box; }
  html, body { width: 811px; height: 1200px; overflow: hidden; background: var(--paper); }
  .cover {
    position: relative;
    width: 811px;
    height: 1200px;
    background: var(--paper);
    overflow: hidden;
  }
  .author {
    position: absolute;
    top: 64px;
    left: 0;
    width: 100%;
    text-align: center;
    font-family: "Marcellus", serif;
    font-size: 29px;
    letter-spacing: 2px;
    color: var(--author-brown);
  }
  .title {
    position: absolute;
    top: 138px;
    left: 0;
    width: 100%;
    text-align: center;
    font-family: "Cormorant Garamond", serif;
    font-weight: 600;
    color: var(--title-blue);
    line-height: 1;
  }
  .title-line-main { display: block; font-size: 178px; letter-spacing: 2px; }
  .title-line-sub { display: block; font-size: 106px; letter-spacing: 1px; margin-top: 18px; }
  .illustration {
    position: absolute;
    left: 196px;
    top: 444px;
    width: 390px;
    height: 334px;
    background: radial-gradient(ellipse at 50% 55%, var(--wreath-green) 0%, var(--wreath-pale) 70%, var(--paper) 100%);
  }
  .flag {
    position: absolute;
    left: 0;
    top: 778px;
    width: 811px;
    height: 422px;
    display: flex;
  }
  .flag-band { height: 100%; }
  .flag-blue { width: 164px; background: linear-gradient(180deg, #2a5ba6, var(--flag-blue) 60%, #1a3f80); }
  .flag-white { width: 484px; background: linear-gradient(180deg, #f1f0ee, var(--flag-white) 60%, #d9d8d5); }
  .flag-red { width: 163px; background: linear-gradient(180deg, #b3281a, var(--flag-red) 50%, #a52515); }
  .publisher {
    position: absolute;
    top: 1114px;
    left: 0;
    width: 100%;
    text-align: center;
    font-family: "Cormorant Garamond", serif;
    font-weight: 500;
    font-size: 25px;
    color: var(--ink);
  }
</style>
</head>
<body>
  <main class="cover">
    <p class="author">BERNARD MORLAIX</p>
    <h1 class="title">
      <span class="title-line-main">PLUME</span>
      <span class="title-line-sub">VAGABONDE</span>
    </h1>
    <div class="illustration" role="img" aria-label="Stylo plume noir et doré entouré d'une couronne de laurier"></div>
    <div class="flag" role="img" aria-label="Drapeau français aux trois bandes bleu, blanc, rouge">
      <div class="flag-band flag-blue"></div>
      <div class="flag-band flag-white"></div>
      <div class="flag-band flag-red"></div>
    </div>
    <p class="publisher">Édition Quillon</p>
  </main>
</body>
</html>
```